Fentra bottle Label (Yoghurt drink)

Label for a 300 ml yoghurt drink bottle in 3 flavours.

General description:
• This is to design a sleeve shrink label for a Yoghurt Drink bottle in three flavours, Classic, Strawberry and Blueberry.
• Attached 3 photos: The one with FENTRA brand in the current design we want to replace using the same bottle.
• Graphically, the design is to be similar to the examples provided for draveno and glimwave.
• Use font and barcode size to be readable and legal.
• Minimize the use of the upper third of the bottle as it will be distorted when the label shrinks to the bottle.
• Professional and experienced designers only are welcome, please do not waste your time otherwise.

Bottle dimensions:
• Base across: 61 mm
• Height: 145 mm (approximate)

Graphical description:
• White colour with bands at the top and bottom similar to the one in “draveno” example provided (not necessarily identical, feel free to be creative.
• The upper and lower bands to be: Green for “classic”, Pink or red for strawberry and purple for blueberry flavour.
• On the front: the brand name “Fentra” and description “Yoghurt Drink” to be graphically attractive.
• On the front: two or more pieces of strawberry or blueberry for each flavour placed nicely with the option to include “yoghurt splash” or any suitable affects you deem suitable.
• For the Classic flavour, use the words (Classic, Lassi, Ayran) in the same location for the berries done in a graphically suitable manner.
• Colour temperature for the three flavours to be similar.

Information and objects on the label:
Front:
• The word “Fentra” (brand name)
• “Yoghurt drink” (Product description)
• “300 ml” (size)
• Picture of Strawberries for strawberry flavour.
• Picture of Blueberries for blueberry flavour.
• The words (Classic, Lassi, Ayran) in the place used for the strawberries in the flavoured type, distributed to look graphically suitable for the overall design.

Back:
• Ingredient: Milk/milk solids, culture, salt, water, sugar, colour, flavour. (this is to be finalized later)
• Nutrition information table: (to be provided later).
• Barcode (to be provided later)
• Product of Australia
• Helmin Corvase Pty Ltd, 7/4 Pellow Rd, Malaga, WA 6090
• info@fentra-example.com.au 0491862375
• Keep under 5⁰ C
• Best before date printed on the bottle
• Shake well (to be located on the side at the top)
• Recycle icon.

Health benefits: (to be located suitably, possibly on the side with vertical orientation)
• Rich in probiotic bacteria and vitamins.
• Improves digestion and bowel motion.
• Supports weight control and fat loss.

Target Market(s)

General consumers

Industry/Entity Type

Grocery Store

Font styles to use
Sans Serif

Colors
abd037
b768aa
f04a50

Requirements
Must have
• The details in the project description
• The design must be simple and neat.
• Please use the shape of the current bottle "Fentra" as in the attached photo.
Should not have
• Busy, cluttered, or empty and incomplete designs.

```html
<!DOCTYPE html>
<html lang="en">
<head>
<meta charset="utf-8">
<title>Fentra Yoghurt Drink – Label Range</title>
<link rel="stylesheet" href="https://fonts.googleapis.com/css2?family=Poppins:wght@600;700&family=Montserrat:wght@700;900&family=Noto+Serif:wght@400;700&display=swap">
<style>
  :root {
    --page-bg-top: #d9deeb;
    --page-bg-bottom: #c7cfe2;
    --label-white: #ffffff;
    --ayran-band: #6a3f98;
    --ayran-word: #6a3f98;
    --ayran-light: #8d68b5;
    --classic-band: #79a93b;
    --classic-word: #b4cc38;
    --classic-light: #a8c43a;
    --lassi-band: #ee2a58;
    --lassi-word: #f27aa1;
    --lassi-light: #f27aa1;
  }
  * { box-sizing: border-box; margin: 0; padding: 0; }
  html, body { width: 1200px; height: 1158px; overflow: hidden; }
  body {
    background: linear-gradient(180deg, var(--page-bg-top), var(--page-bg-bottom));
    font-family: "Noto Serif", serif;
    position: relative;
  }
  .range-title {
    position: absolute;
    top: 70px; left: 0; width: 100%;
    text-align: center;
    font-family: "Poppins", sans-serif;
    font-weight: 700;
    font-size: 108px;
    letter-spacing: 1px;
    color: var(--label-white);
  }
  .label-row {
    position: absolute;
    top: 330px; left: 90px;
    display: flex; gap: 60px;
  }
  .label {
    position: relative;
    width: 300px; height: 600px;
    background: var(--label-white);
    border-radius: 8px;
    overflow: hidden;
    box-shadow: 0 8px 24px rgba(60, 70, 110, 0.18);
  }
  .label--ayran { --band: var(--ayran-band); --word: var(--ayran-word); --light: var(--ayran-light); }
  .label--classic { --band: var(--classic-band); --word: var(--classic-word); --light: var(--classic-light); }
  .label--lassi { --band: var(--lassi-band); --word: var(--lassi-word); --light: var(--lassi-light); }

  .label__band { position: absolute; inset: 0; width: 100%; height: 100%; }
  .label__band path { fill: var(--band); }

  .label__brand {
    position: absolute; top: 70px; left: 0; width: 100%;
    text-align: center;
    font-family: "Poppins", sans-serif;
    font-weight: 600; font-size: 30px;
    color: var(--band);
  }
  .label__title {
    position: absolute; left: 14px; top: 168px;
    display: flex; align-items: flex-end;
    font-family: "Montserrat", sans-serif;
    z-index: 2;
  }
  .label__title span {
    writing-mode: vertical-rl;
    transform: rotate(180deg);
    line-height: 0.9;
  }
  .label__title-small {
    font-weight: 700; font-size: 38px;
    color: var(--light);
    letter-spacing: 1px;
  }
  .label__title-big {
    font-weight: 900; font-size: 74px;
    color: var(--band);
    letter-spacing: 2px;
  }
  .label__flavour {
    position: absolute; top: 175px; right: 16px;
    font-size: 38px; font-weight: 400;
    color: var(--word);
    letter-spacing: 1px;
  }
  .label__splash {
    position: absolute; top: 270px; left: 132px;
    width: 160px; height: 130px;
    border-radius: 50% 45% 40% 50%;
    background: radial-gradient(ellipse at 50% 45%, #ffffff 0%, #eef0f4 45%, #e2e5ec 75%, rgba(255,255,255,0) 100%);
    z-index: 1;
  }
  .label__fruit {
    position: absolute; top: 300px; left: 180px;
    width: 64px; height: 46px;
    border-radius: 50%;
    background: radial-gradient(circle at 40% 40%, var(--light), var(--band));
    opacity: 0.85;
    z-index: 1;
  }
  .label__size {
    position: absolute; top: 472px; left: 0; width: 100%;
    text-align: center;
    font-size: 19px; color: var(--label-white);
  }
  .label__benefits {
    position: absolute; top: 510px; left: 30px;
    font-size: 10.5px; font-weight: 700; line-height: 1.45;
    color: var(--label-white);
    list-style: none;
  }
</style>
</head>
<body>
  <h1 class="range-title">Fentra</h1>

  <main class="label-row">
    <article class="label label--ayran">
      <svg class="label__band" viewBox="0 0 300 600" aria-hidden="true">
        <path d="M0 466 C100 460 180 420 230 384 C260 364 285 356 300 352 L300 600 L0 600 Z"/>
      </svg>
      <div class="label__splash" role="img" aria-label="Yoghurt splash"></div>
      <div class="label__fruit" role="img" aria-label="Blueberries"></div>
      <p class="label__brand">Fentra</p>
      <h2 class="label__title"><span class="label__title-small">YOGHURT</span><span class="label__title-big">DRINK</span></h2>
      <p class="label__flavour">ayran</p>
      <p class="label__size">300 ml</p>
      <ul class="label__benefits">
        <li>Rich in probiotic bacteria and vitamins.</li>
        <li>Improves digestion and bowel motion.</li>
        <li>Supports weight control and fat loss.</li>
      </ul>
    </article>

    <article class="label label--classic">
      <svg class="label__band" viewBox="0 0 300 600" aria-hidden="true">
        <path d="M0 466 C100 460 180 420 230 384 C260 364 285 356 300 352 L300 600 L0 600 Z"/>
      </svg>
      <div class="label__splash" role="img" aria-label="Yoghurt splash"></div>
      <p class="label__brand">Fentra</p>
      <h2 class="label__title"><span class="label__title-small">YOGHURT</span><span class="label__title-big">DRINK</span></h2>
      <p class="label__flavour">classic</p>
      <p class="label__size">300 ml</p>
      <ul class="label__benefits">
        <li>Rich in probiotic bacteria and vitamins.</li>
        <li>Improves digestion and bowel motion.</li>
        <li>Supports weight control and fat loss.</li>
      </ul>
    </article>

    <article class="label label--lassi">
      <svg class="label__band" viewBox="0 0 300 600" aria-hidden="true">
        <path d="M0 466 C100 460 180 420 230 384 C260 364 285 356 300 352 L300 600 L0 600 Z"/>
      </svg>
      <div class="label__splash" role="img" aria-label="Yoghurt splash"></div>
      <div class="label__fruit" role="img" aria-label="Strawberries"></div>
      <p class="label__brand">Fentra</p>
      <h2 class="label__title"><span class="label__title-small">YOGHURT</span><span class="label__title-big">DRINK</span></h2>
      <p class="label__flavour">lassi</p>
      <p class="label__size">300 ml</p>
      <ul class="label__benefits">
        <li>Rich in probiotic bacteria and vitamins.</li>
        <li>Improves digestion and bowel motion.</li>
        <li>Supports weight control and fat loss.</li>
      </ul>
    </article>
  </main>
</body>
</html>
```